依頼詳細
コロナ禍ですが、陽気回転 Merry Tumbelという愛称を両方付けて遊び心を入れたいです。商標登録申請済み。ー この部分のデザインは私の手元にファイルとしてあります。ー 全体はクリスマス商戦に先だって売り出したいので、その季節に合う赤系統を全体の色で。ただし 春の足音が聞こえて来たら全体色は替えるかも知れません。ー 状況によりけり ー
記載項目
化粧箱には 製造元や販売元 その他健福省が定めた様々なテキストを入れる必要がありますが、これは キャラメル箱の背面に一括でこちらで入れるので 今回依頼のデザインには関係ありません。
記載事項などでデザイン依頼するのは 全体の色(単色でなくても可) と 陽気回転 Merry Tumble という文字の色 箱表面における配置などです。尚、商標登録申請したデザインは私の手元にありますが、これをお送りしてそれを微修正して使ってください。
希望イメージ
シンプル 複雑
単色 カラフル
暗い 明るい
日常 高級
遊び心 厳粛
未来的 伝統的
女性的 男性的
希望する色
赤系
納品ファイル
• 高解像度JPG (.jpg)
補足説明
商標のデザインのファイルを添付しましたが、これをそのまま使うのではなく 文字の"跳ね"は維持しつつ 文字の色 フォント 水玉の色などは適宜修正して構いません。

このパッケージのキーである「陽気回転」の文字が目立つようなデザインで、しかも全体が明るい雰囲気となっている。

ありがとうございました。何回か修正を依頼させていただきましたが、それに十分に応えていただき感謝いたします。

```html
<!DOCTYPE html>
<html lang="en">
<head>
<meta charset="utf-8">
<title>Merry Tumble – Package Front</title>
<link href="https://fonts.googleapis.com/css2?family=Comfortaa:wght@500&display=swap" rel="stylesheet">
<style>
  :root {
    --page-bg: #ffffff;
    --lip-red: #c9353d;
    --lip-rose: #e39a98;
    --lip-blush: #f3d3d1;
    --lip-paper: #f9ecec;
    --label-red: #b8283a;
    --label-line: #ffffff;
    --ink-light: #ffffff;
    --art-tone: #d97f86;
  }
  html, body {
    margin: 0;
    padding: 0;
    width: 744px;
    height: 1200px;
    overflow: hidden;
    background: var(--page-bg);
  }
  .canvas {
    position: relative;
    width: 744px;
    height: 1200px;
    display: flex;
    align-items: center;
    justify-content: center;
  }
  .package-front {
    position: relative;
    width: 520px;
    height: 520px;
  }
  .lip-pattern {
    position: absolute;
    inset: 0;
    background:
      radial-gradient(circle at 20% 25%, var(--lip-red) 0 12%, transparent 30%),
      radial-gradient(circle at 80% 20%, var(--lip-rose) 0 10%, transparent 28%),
      radial-gradient(circle at 15% 80%, var(--lip-rose) 0 10%, transparent 28%),
      radial-gradient(circle at 85% 75%, var(--lip-red) 0 12%, transparent 30%),
      linear-gradient(135deg, var(--lip-blush), var(--lip-paper) 50%, var(--lip-blush));
  }
  .brand-label {
    position: absolute;
    left: 140px;
    top: 128px;
    width: 240px;
    height: 336px;
    background: var(--label-red);
    box-sizing: border-box;
    padding: 10px;
  }
  .brand-label__frame {
    width: 100%;
    height: 100%;
    border: 2px solid var(--label-line);
    box-sizing: border-box;
    display: flex;
    flex-direction: column;
    align-items: center;
  }
  .dreamcatcher-art {
    margin-top: 18px;
    width: 126px;
    height: 212px;
    border-radius: 63px 63px 20px 20px;
    background: linear-gradient(180deg, var(--art-tone), var(--label-red));
  }
  .brand-name {
    margin: auto 0 24px;
    font-family: "Comfortaa", sans-serif;
    font-weight: 500;
    font-size: 27px;
    line-height: 1;
    letter-spacing: 0.3px;
    color: var(--ink-light);
    white-space: nowrap;
    text-transform: lowercase;
  }
</style>
</head>
<body>
  <main class="canvas">
    <section class="package-front">
      <div class="lip-pattern" role="img" aria-label="Repeating pattern of red and pink lip prints"></div>
      <div class="brand-label">
        <div class="brand-label__frame">
          <div class="dreamcatcher-art" role="img" aria-label="White line illustration of a dreamcatcher with hanging feathers"></div>
          <p class="brand-name">merry tumble</p>
        </div>
      </div>
    </section>
  </main>
</body>
</html>
```